Larkspire School of Music Website Design

Larkspire School of Music would like to have a website designed. They are a new business similar to Torvale (https://torvaletunes.example).

We prefer using Adobe Fonts throughout the design. Kepler was used for the logo. Lorem Ipsum is fine to use except for headers.

Please keep track of any images/icons that are used in your design. We plan on purchasing the images used in the winning design.

Target Market(s)

Children age 10 - 18

Number of Pages Required

1 page

Font styles to use
Sans Serif

Colors
0054AA
0677BA
7BADD7
CADEEF
E8F1F8

```html
<!DOCTYPE html>
<html lang="en">
<head>
<meta charset="utf-8">
<title>Larkspire School of Music</title>
<link href="https://fonts.googleapis.com/css2?family=Crimson+Pro:wght@600;700;800&family=Roboto:wght@400;500;700&display=swap" rel="stylesheet">
<style>
:root{
  --blue:#0054AA;--mid:#0677BA;--sky:#7BADD7;--pale:#CADEEF;--ice:#E8F1F8;
  --navy:#0f2348;--ink:#1a2a4a;--text:#555d6b;--white:#fff;--gold:#f5b82e;
  --serif:"Crimson Pro",Georgia,serif;--sans:"Roboto",Arial,sans-serif;
}
*{box-sizing:border-box;margin:0;padding:0}
html,body{width:1200px;height:3788px;overflow:hidden}
body{font-family:var(--sans);color:var(--text);background:var(--white);position:relative}
section,header,footer{position:absolute;left:0;width:1200px}
.abs{position:absolute}
.btn{display:inline-block;font:500 12px var(--sans);padding:10px 22px;border-radius:3px;background:var(--blue);color:var(--white);letter-spacing:.5px}
.btn-sm{font-size:10px;padding:7px 16px}
.h2{font:800 34px var(--serif);color:var(--navy);text-align:center;letter-spacing:1px}
.rule{width:70px;height:3px;background:var(--blue);margin:10px auto 18px}
.lead{width:640px;margin:0 auto;text-align:center;font-size:13px;line-height:1.6}
.ph{border-radius:2px}

/* header & hero */
.hero{top:0;height:600px;background:linear-gradient(90deg,#f4f4f2 0,#f4f4f2 35%,#e9e6e1 100%)}
.hero-photo{left:430px;top:0;width:770px;height:600px;background:linear-gradient(120deg,#eae6df 0%,#d8c3a8 35%,#9a7656 60%,#c9ccd3 100%)}
.brand{left:36px;top:8px;display:flex;align-items:center;gap:10px}
.brand-mark{width:34px;height:34px;border-radius:50%;background:var(--blue)}
.brand-name{font:700 22px var(--serif);color:var(--blue);line-height:1}
.brand-sub{font:600 9px var(--serif);color:var(--blue);letter-spacing:2px}
.follow{right:40px;top:10px;display:flex;gap:6px;align-items:center;font-size:10px;color:var(--navy);font-weight:500}
.follow span.sq{width:16px;height:16px;background:var(--blue);border-radius:2px}
.nav{left:440px;top:56px;display:flex;gap:26px;font-size:11px;color:var(--navy)}
.nav .on{color:var(--blue);font-weight:700}
.cta{right:40px;top:48px;display:flex;gap:10px}
.btn-out{background:var(--white);color:var(--blue);border:1px solid var(--blue)}
.hero-title{left:40px;top:170px;font:800 50px/1.02 var(--serif);color:var(--navy);letter-spacing:1px}
.hero-copy{left:40px;top:352px;width:330px;font-size:12px;line-height:1.5;color:var(--ink)}
.hero-btn{left:40px;top:420px}

/* programs */
.programs{top:600px;height:640px;padding-top:88px}
.cards{position:absolute;left:128px;top:232px;display:flex;gap:30px}
.card{width:208px;padding:0 0 18px}
.card.feat{background:var(--blue);padding:8px 8px 18px;margin-top:-8px;width:216px}
.card .img{height:164px}
.card h3{font:700 17px var(--serif);color:var(--navy);margin:22px 0 8px}
.card.feat h3,.card.feat p{color:var(--white)}
.card p{font-size:11px;line-height:1.5;margin-bottom:12px}
.card.feat .btn{background:var(--white);color:var(--blue)}

/* about */
.about{top:1240px;height:500px;background:var(--ice)}
.about-ring{left:140px;top:60px;width:400px;height:400px;border-radius:50%;border:4px solid var(--sky)}
.about-photo{left:160px;top:72px;width:380px;height:380px;border-radius:50%;background:linear-gradient(135deg,#b9a58b,#6f5a44 55%,#3f5a7a)}
.dot{border-radius:50%;background:var(--pale)}
.about-text{left:632px;top:90px;width:470px}
.eyebrow{font:700 11px var(--sans);color:var(--blue);letter-spacing:1px}
.about-text h2{font:800 44px var(--serif);color:var(--navy);letter-spacing:1px;margin:4px 0 6px}
.about-text .rule{margin:0 0 20px;width:80px}
.about-text p{font-size:12px;line-height:1.6;margin-bottom:14px}

/* numbers */
.numbers{top:1740px;height:452px;background:var(--blue);color:var(--white);text-align:center;padding-top:70px}
.numbers .h2{color:var(--white)}
.numbers .rule{background:var(--white)}
.big{font:800 34px var(--serif)}
.big-cap{font-size:12px;margin-top:2px}
.stats{position:absolute;left:140px;top:230px;display:flex;width:920px;justify-content:space-between}
.stat{width:200px}
.ico{width:60px;height:60px;border:2px solid var(--white);border-radius:8px;margin:0 auto 20px;display:flex;align-items:center;justify-content:center}
.stat .val{font:800 32px var(--serif)}
.stat .cap{font-size:11px;line-height:1.4;margin-top:6px;opacity:.9}

/* testimonials */
.testi{top:2192px;height:540px;padding-top:70px}
.tcards{position:absolute;left:140px;top:200px;display:flex;gap:34px}
.tcard{width:320px;height:250px;background:var(--white);box-shadow:0 4px 18px rgba(0,40,90,.14);padding:22px 24px;position:relative}
.who{display:flex;align-items:center;gap:12px;margin-bottom:22px}
.avatar{width:44px;height:44px;border-radius:50%;background:linear-gradient(135deg,#c7b8a8,#7d6a5a)}
.who b{display:block;font:700 13px var(--sans);color:var(--ink)}
.who small{font-size:10px}
.stars{position:absolute;right:22px;top:34px;display:flex;gap:2px}
.tcard p{font-size:12px;line-height:1.6}
.tcard p b{color:var(--ink)}
.quote{position:absolute;right:22px;bottom:12px;font:800 70px/1 var(--serif);color:var(--pale)}
.pager{position:absolute;left:560px;top:486px;display:flex;gap:14px}
.pager span{width:32px;height:32px;border-radius:50%;border:1px solid var(--pale);display:flex;align-items:center;justify-content:center;font-size:12px;color:var(--blue)}
.pager span.on{background:var(--blue);color:var(--white)}

/* news */
.news{top:2732px;height:608px;padding-top:60px;border-top:1px solid var(--ice)}
.ncards{position:absolute;left:168px;top:190px;display:flex;gap:40px}
.ncard{width:262px}
.ncard .img{height:196px}
.ncard h3{font:700 18px var(--serif);color:var(--navy);margin:16px 0 6px}
.meta{font-size:11px;color:var(--ink);margin-bottom:8px}
.ncard p{font-size:11px;line-height:1.5}
.ncard p b{color:var(--ink)}

/* footer */
.footer{top:3340px;height:448px;background:var(--navy);color:#c9d3e3}
.f-brand{left:164px;top:56px;width:260px}
.f-brand .brand-mark{background:var(--sky);margin-bottom:10px;width:44px;height:44px}
.f-brand .brand-name{color:var(--white);font-size:28px}
.f-brand .brand-sub{color:var(--white)}
.f-brand p{font-size:11px;line-height:1.6;margin-top:14px}
.fcol{top:64px}
.fcol h4{font:700 13px var(--sans);color:var(--white);margin-bottom:14px}
.fcol li{list-style:none;font-size:11px;line-height:2}
.news-in{width:230px;height:34px;background:var(--white);border-radius:2px;margin-bottom:10px}
.f-bottom{left:0;top:400px;width:1200px;height:48px;border-top:1px solid #25396a;display:flex;justify-content:space-between;align-items:center;padding:0 164px;font-size:10px}
</style>
</head>
<body>

<header class="hero">
  <div class="abs hero-photo" role="img" aria-label="Photo of a teacher guiding a young student playing the violin"></div>
  <div class="abs brand"><span class="brand-mark"></span><div><div class="brand-name">LARKSPIRE</div><div class="brand-sub">SCHOOL OF MUSIC</div></div></div>
  <div class="abs follow">Follow Us <span class="sq"></span><span class="sq"></span><span class="sq"></span><span class="sq"></span></div>
  <nav class="abs nav"><span class="on">Home</span><span>About Us</span><span>Our Impact</span><span>Support Torvale</span><span>Student Resources</span></nav>
  <div class="abs cta"><span class="btn btn-sm">Register</span><span class="btn btn-sm btn-out">Donate</span></div>
  <h1 class="abs hero-title">SIGN UP FOR<br>SPRING CLASSES<br>BY JAN 14!</h1>
  <p class="abs hero-copy">Lorem ipsum dolor sit amet, consectetur adipiscing elit sed do eiusmod tempor incididunt ut labore.</p>
  <span class="abs btn hero-btn">REGISTER TODAY</span>
</header>

<section class="programs">
  <h2 class="h2">OUR PROGRAMS</h2>
  <div class="rule"></div>
  <p class="lead">Lorem ipsum dolor sit amet, consectetur adipiscing elit, sed do eiusmod tempor incididunt ut labore et dolore magna aliqua ut enim ad minim veniam quis nostrud exercitation.</p>
  <div class="cards">
    <div class="card"><div class="img ph" role="img" aria-label="Photo of young children in an early music class" style="background:linear-gradient(135deg,#7BADD7,#0054AA)"></div><h3>Early Childhood</h3><p>Lorem ipsum dolor sit amet, consectetur adipiscing elit sed eiusmod tempor incididunt.</p><span class="btn btn-sm">Learn More</span></div>
    <div class="card feat"><div class="img ph" role="img" aria-label="Photo of a student in a private instrument lesson" style="background:linear-gradient(135deg,#e9d27a,#b8902e)"></div><h3>Private Lessons</h3><p>Lorem ipsum dolor sit amet, consectetur adipiscing elit sed eiusmod tempor incididunt.</p><span class="btn btn-sm">Learn More</span></div>
    <div class="card"><div class="img ph" role="img" aria-label="Photo of a group music class" style="background:linear-gradient(135deg,#f06fb8,#c3177e)"></div><h3>Group Classes</h3><p>Lorem ipsum dolor sit amet, consectetur adipiscing elit sed eiusmod tempor incididunt.</p><span class="btn btn-sm">Learn More</span></div>
    <div class="card"><div class="img ph" role="img" aria-label="Photo of kids at an outdoor summer music camp" style="background:linear-gradient(135deg,#8fd36a,#2f8a2a)"></div><h3>Summer Camps</h3><p>Lorem ipsum dolor sit amet, consectetur adipiscing elit sed eiusmod tempor incididunt.</p><span class="btn btn-sm">Learn More</span></div>
  </div>
</section>

<section class="about">
  <div class="abs about-ring"></div>
  <div class="abs dot" style="left:128px;top:380px;width:26px;height:26px"></div>
  <div class="abs dot" style="left:504px;top:92px;width:18px;height:18px"></div>
  <div class="abs about-photo" role="img" aria-label="Photo of a teacher and student playing guitars together"></div>
  <div class="abs about-text">
    <div class="eyebrow">LARKSPIRE SCHOOL OF MUSIC</div>
    <h2>ABOUT US</h2>
    <div class="rule"></div>
    <p>Lorem ipsum dolor sit amet, consectetur adipiscing elit, sed do eiusmod tempor incididunt ut labore et dolore magna aliqua. Ut enim ad minim veniam, quis nostrud exercitation.</p>
    <p>Lorem ipsum dolor sit amet, consectetur adipiscing elit sed do eiusmod tempor incididunt ut labore.</p>
    <p>Duis aute irure dolor in reprehenderit in voluptate velit esse cillum dolore eu fugiat nulla pariatur. Excepteur sint occaecat cupidatat non proident.</p>
    <span class="btn btn-sm">Learn More</span>
  </div>
</section>

<section class="numbers">
  <h2 class="h2">TORVALE BY THE NUMBERS</h2>
  <div class="rule"></div>
  <div class="big">2,500+</div>
  <div class="big-cap">Students Engaged Annually</div>
  <div class="stats">
    <div class="stat"><div class="ico"><svg width="30" height="30" viewBox="0 0 30 30" fill="none" stroke="#fff" stroke-width="2"><circle cx="15" cy="15" r="11"/><path d="M15 8v14M11 11h6a3 3 0 0 1 0 6h-4a3 3 0 0 0 0 6h6"/></svg></div><div class="val">$1.4 million</div><div class="cap">in financial aid and direct student support provided</div></div>
    <div class="stat"><div class="ico"><svg width="30" height="30" viewBox="0 0 30 30" fill="none" stroke="#fff" stroke-width="2"><path d="M11 23V7l12-3v16"/><circle cx="8" cy="23" r="3"/><circle cx="20" cy="20" r="3"/></svg></div><div class="val">25</div><div class="cap">Programs across partner sites</div></div>
    <div class="stat"><div class="ico"><svg width="30" height="30" viewBox="0 0 30 30" fill="none" stroke="#fff" stroke-width="2"><path d="M3 12l12-6 12 6-12 6z"/><path d="M8 15v6c4 3 10 3 14 0v-6"/></svg></div><div class="val">100%</div><div class="cap">of students who completed the program graduated on time</div></div>
    <div class="stat"><div class="ico"><svg width="30" height="30" viewBox="0 0 30 30" fill="none" stroke="#fff" stroke-width="2"><circle cx="15" cy="15" r="11"/><path d="M10 15l4 4 7-8"/></svg></div><div class="val">60%</div><div class="cap">of students continue playing music after the first year</div></div>
  </div>
</section>

<section class="testi">
  <h2 class="h2">CLIENT TESTIMONIALS</h2>
  <div class="rule"></div>
  <p class="lead">Lorem ipsum dolor sit amet, consectetur adipiscing elit, sed do eiusmod tempor incididunt ut labore et dolore magna aliqua.</p>
  <div class="tcards">
    <div class="tcard"><div class="who"><span class="avatar"></span><div><b>Harlan Voss, MBA</b><small>Company Name</small></div></div><div class="stars"><svg width="64" height="12" viewBox="0 0 64 12" fill="#f5b82e"><path id="s" d="M6 0l1.8 3.8 4.2.5-3.1 2.9.8 4.1L6 9.3 2.3 11.3l.8-4.1L0 4.3l4.2-.5z"/><use href="#s" x="13"/><use href="#s" x="26"/><use href="#s" x="39"/><use href="#s" x="52"/></svg></div><p>"Lorem ipsum dolor sit amet, consectetur adipiscing elit, sed do eiusmod tempor incididunt ut labore et dolore magna aliqua. Ut enim ad minim veniam, quis nostrud exercitation ullamco laboris nisi ut aliquip... <b>Read More</b></p><span class="quote">&rdquo;</span></div>
    <div class="tcard"><div class="who"><span class="avatar"></span><div><b>Milo Hartwell</b><small>Company Name</small></div></div><div class="stars"><svg width="64" height="12" viewBox="0 0 64 12" fill="#f5b82e"><use href="#s"/><use href="#s" x="13"/><use href="#s" x="26"/><use href="#s" x="39"/><use href="#s" x="52"/></svg></div><p>"Lorem ipsum dolor sit amet, consectetur adipiscing elit, sed do eiusmod tempor incididunt ut labore et dolore magna aliqua. Ut enim ad minim veniam, quis nostrud exercitation ullamco laboris nisi ut aliquip... <b>Read More</b></p><span class="quote">&rdquo;</span></div>
    <div class="tcard"><div class="who"><span class="avatar"></span><div><b>Tobias Prent &amp; Theo</b><small>Company Name</small></div></div><div class="stars"><svg width="64" height="12" viewBox="0 0 64 12" fill="#f5b82e"><use href="#s"/><use href="#s" x="13"/><use href="#s" x="26"/><use href="#s" x="39"/><use href="#s" x="52"/></svg></div><p>"Lorem ipsum dolor sit amet, consectetur adipiscing elit, sed do eiusmod tempor incididunt ut labore et dolore magna aliqua. Ut enim ad minim veniam, quis nostrud exercitation ullamco laboris nisi ut aliquip... <b>Read More</b></p><span class="quote">&rdquo;</span></div>
  </div>
  <div class="pager"><span>&larr;</span><span class="on">&rarr;</span></div>
</section>

<section class="news">
  <h2 class="h2">WHAT'S HAPPENING?</h2>
  <div class="rule"></div>
  <p class="lead">Lorem ipsum dolor sit amet, consectetur adipiscing elit, sed do eiusmod tempor incididunt ut labore et dolore magna aliqua.</p>
  <div class="ncards">
    <div class="ncard"><div class="img ph" role="img" aria-label="Photo of a classroom music lesson" style="background:linear-gradient(135deg,#d9c6a4,#8a6a48)"></div><h3>Lorem ipsum consectetur</h3><div class="meta">December 8, 2022 &nbsp;|&nbsp; 2 minutes</div><p>Lorem ipsum dolor sit amet, consectetur adipiscing elit, sed do eiusmod tempor incididunt ut labore et dolore... <b>Read More</b></p></div>
    <div class="ncard"><div class="img ph" role="img" aria-label="Colourful illustration of a child with musical notes" style="background:linear-gradient(135deg,#2b3a8c,#e0489a 50%,#f7c64a)"></div><h3>Lorem ipsum consectetur</h3><div class="meta">December 8, 2022 &nbsp;|&nbsp; 2 minutes</div><p>Lorem ipsum dolor sit amet, consectetur adipiscing elit, sed do eiusmod tempor incididunt ut labore et dolore... <b>Read More</b></p></div>
    <div class="ncard"><div class="img ph" role="img" aria-label="Photo of children playing instruments together" style="background:linear-gradient(135deg,#e9d9c0,#b07e5a 60%,#6b8fb8)"></div><h3>Lorem ipsum consectetur</h3><div class="meta">December 8, 2022 &nbsp;|&nbsp; 2 minutes</div><p>Lorem ipsum dolor sit amet, consectetur adipiscing elit, sed do eiusmod tempor incididunt ut labore et dolore... <b>Read More</b></p></div>
  </div>
</section>

<footer class="footer">
  <div class="abs f-brand"><div class="brand-mark"></div><div class="brand-name">LARKSPIRE</div><div class="brand-sub">SCHOOL OF MUSIC</div><p>Lorem ipsum dolor sit amet, consectetur adipiscing elit, sed do eiusmod tempor incididunt ut labore et dolore.</p></div>
  <div class="abs fcol" style="left:452px"><h4>Quick Links</h4><ul><li>Home</li><li>About Us</li><li>Our Impact</li><li>Support Torvale</li><li>Student Resources</li></ul></div>
  <div class="abs fcol" style="left:640px"><h4>Other Link</h4><ul><li>Our Team</li><li>Latest News</li><li>Contact Us</li><li>FAQ</li></ul></div>
  <div class="abs fcol" style="left:808px"><h4>Newsletter</h4><div class="news-in"></div><span class="btn btn-sm">Submit Now</span></div>
  <div class="abs f-bottom"><span>Copyright &copy; 2023 Larkspire School of Music. All rights reserved.</span><span>Privacy Policy &nbsp;|&nbsp; Terms &amp; Condition</span></div>
</footer>

</body>
</html>
```